Hispanic Financial Counseling and Advocate Firm seeks business card design

Looking for a clean, professional business card design. This is a firm that specializes in providing financial education, coaching, and planning to the Hispanic community. The name of the company is Valendo, which means to prosper. We need a design that is clean, professional, and invokes trust, professionalism, but also welcoming. Our logo is a plant growing from a hand to give the messaging of of being in control of growing your financial future and security. Its part of a larger organization names Cresta Financial Group, who's logo is a tree with multi colored branches. We have the back of the card designed so we just need the front designed. the back is blue, so front needs to be a different background color, not blue.

Target Market(s)

Hispanic Community looking to better their future

Industry/Entity Type

financial services

Contact Information for Business Card

contact info: Ernesto Villalba Jr, 951-555-4613, info@crestafinancialgroup.example. Crestafinancialgroup.example. tag line: Para un futuro mas seguro!

Requirements
Must have
• basics: logo, contact info.
Nice to have
• possibly incorporate the tree logo provided somehow
Should not have
• should not look like the back, needs to be different from the back provided.

```html
<!DOCTYPE html>
<html lang="es">
<head>
<meta charset="utf-8">
<title>Valendo – Tarjeta de presentación</title>
<link rel="stylesheet" href="https://fonts.googleapis.com/css2?family=Jost:ital,wght@0,500;0,600;1,400;1,700&family=Roboto:ital,wght@1,700&family=Open+Sans:wght@400&display=swap">
<style>
  :root {
    --board-green: #6ca845;
    --shadow-green: #5f993c;
    --brand-green: #6aa641;
    --navy: #4a5270;
    --card-white: #ffffff;
    --card-edge: #222222;
    --mist: #ececec;
    --page: #ffffff;
  }
  * { margin: 0; padding: 0; box-sizing: border-box; }
  html, body { width: 1200px; height: 1109px; overflow: hidden; background: var(--page); }
  .canvas { position: relative; width: 1200px; height: 1109px; }
  .board { position: absolute; left: 190px; top: 0; width: 813px; height: 995px; background: var(--board-green); }
  .option { position: absolute; left: 323px; width: 555px; }
  .option--a { top: 102px; }
  .option--b { top: 569px; }
  .card-shadow { position: absolute; left: 0; top: 321px; width: 555px; height: 28px; }
  .card {
    position: absolute; left: 0; top: 0; width: 555px; height: 321px;
    background: var(--card-white); border: 1px solid var(--card-edge); overflow: hidden;
  }
  .tree-backdrop {
    position: absolute; left: 337px; top: 0; width: 218px; height: 321px;
    background: radial-gradient(ellipse at 75% 55%, var(--mist) 0%, rgba(236,236,236,0.6) 45%, rgba(255,255,255,0) 75%);
  }
  .brand { position: absolute; left: 82px; top: 88px; width: 146px; text-align: center; }
  .brand__dot { display: block; width: 42px; height: 42px; border-radius: 50%; background: var(--brand-green); margin: 0 auto 10px; }
  .brand__name {
    font-family: "Jost", sans-serif; font-weight: 500; font-size: 38px; line-height: 1;
    color: var(--brand-green); letter-spacing: -0.5px;
  }
  .brand__sub {
    margin-top: 6px; font-family: "Jost", sans-serif; font-weight: 600; font-size: 9.4px;
    letter-spacing: 0.9px; color: var(--navy); white-space: nowrap;
  }
  .divider { position: absolute; left: 277px; top: 107px; width: 1px; height: 108px; background: var(--navy); }
  .contact { position: absolute; left: 317px; top: 104px; }
  .contact__name {
    font-family: "Jost", sans-serif; font-style: italic; font-weight: 700; font-size: 17px;
    color: var(--brand-green); letter-spacing: 0.4px; margin-left: 2px;
  }
  .contact__list { list-style: none; margin-top: 33px; }
  .contact__item {
    display: flex; align-items: center; height: 20.7px;
    font-family: "Jost", sans-serif; font-style: italic; font-weight: 400; font-size: 13px;
    color: var(--navy); white-space: nowrap;
  }
  .contact__icon { width: 11px; height: 11px; margin-right: 8px; flex: none; }
  .tagline {
    position: absolute; left: 313px; top: 270px; width: 243px; height: 23px;
    background: var(--brand-green); border-radius: 12px 0 0 12px;
    font-family: "Roboto", sans-serif; font-style: italic; font-weight: 700; font-size: 14px;
    color: var(--card-white); line-height: 23px; padding-left: 21px; letter-spacing: 0.3px;
  }
  .option-label {
    position: absolute; left: 929px; font-family: "Open Sans", sans-serif; font-size: 23px;
    color: var(--card-white); line-height: 1;
  }
  .option-label--a { top: 403px; }
  .option-label--b { top: 871px; }
</style>
</head>
<body>
<div class="canvas">
  <div class="board"></div>

  <section class="option option--a">
    <svg class="card-shadow" viewBox="0 0 555 28" aria-hidden="true"><path d="M0 0H555V28Q277 6 0 28Z" fill="var(--shadow-green)"/></svg>
    <article class="card">
      <div class="tree-backdrop" role="img" aria-label="Faint tree growing from an open hand, background decoration"></div>
      <div class="brand">
        <span class="brand__dot"></span>
        <div class="brand__name">Valendo</div>
        <div class="brand__sub">SERVICIOS FINANCIEROS</div>
      </div>
      <div class="divider"></div>
      <div class="contact">
        <h1 class="contact__name">ERNESTO VILLALBA JR</h1>
        <ul class="contact__list">
          <li class="contact__item"><svg class="contact__icon" viewBox="0 0 12 12"><circle cx="6" cy="6" r="6" fill="var(--brand-green)"/><path d="M4 3.2l1 1.4-.6.7c.4.9 1.1 1.6 2 2l.7-.6 1.4 1-.6 1c-2.3-.3-4.3-2.3-4.6-4.6z" fill="#fff"/></svg>951-555-4613,</li>
          <li class="contact__item"><svg class="contact__icon" viewBox="0 0 12 12"><circle cx="6" cy="6" r="6" fill="var(--brand-green)"/><rect x="3" y="4" width="6" height="4.2" fill="none" stroke="#fff" stroke-width="0.8"/><path d="M3 4l3 2.3L9 4" fill="none" stroke="#fff" stroke-width="0.8"/></svg>info@crestafinancialgroup.example.</li>
          <li class="contact__item"><svg class="contact__icon" viewBox="0 0 12 12"><circle cx="6" cy="6" r="6" fill="var(--brand-green)"/><circle cx="6" cy="6" r="3.2" fill="none" stroke="#fff" stroke-width="0.7"/><path d="M2.8 6h6.4M6 2.8c-1.6 2-1.6 4.4 0 6.4M6 2.8c1.6 2 1.6 4.4 0 6.4" fill="none" stroke="#fff" stroke-width="0.6"/></svg>Crestafinancialgroup.example.</li>
        </ul>
      </div>
      <div class="tagline">Para un futuro mas seguro!</div>
    </article>
  </section>
  <div class="option-label option-label--a">A</div>

  <section class="option option--b">
    <svg class="card-shadow" viewBox="0 0 555 28" aria-hidden="true"><path d="M0 0H555V28Q277 6 0 28Z" fill="var(--shadow-green)"/></svg>
    <article class="card">
      <div class="brand">
        <span class="brand__dot"></span>
        <div class="brand__name">Valendo</div>
        <div class="brand__sub">SERVICIOS FINANCIEROS</div>
      </div>
      <div class="divider"></div>
      <div class="contact">
        <h2 class="contact__name">ERNESTO VILLALBA JR</h2>
        <ul class="contact__list">
          <li class="contact__item"><svg class="contact__icon" viewBox="0 0 12 12"><circle cx="6" cy="6" r="6" fill="var(--brand-green)"/><path d="M4 3.2l1 1.4-.6.7c.4.9 1.1 1.6 2 2l.7-.6 1.4 1-.6 1c-2.3-.3-4.3-2.3-4.6-4.6z" fill="#fff"/></svg>951-555-4613,</li>
          <li class="contact__item"><svg class="contact__icon" viewBox="0 0 12 12"><circle cx="6" cy="6" r="6" fill="var(--brand-green)"/><rect x="3" y="4" width="6" height="4.2" fill="none" stroke="#fff" stroke-width="0.8"/><path d="M3 4l3 2.3L9 4" fill="none" stroke="#fff" stroke-width="0.8"/></svg>info@crestafinancialgroup.example.</li>
          <li class="contact__item"><svg class="contact__icon" viewBox="0 0 12 12"><circle cx="6" cy="6" r="6" fill="var(--brand-green)"/><circle cx="6" cy="6" r="3.2" fill="none" stroke="#fff" stroke-width="0.7"/><path d="M2.8 6h6.4M6 2.8c-1.6 2-1.6 4.4 0 6.4M6 2.8c1.6 2 1.6 4.4 0 6.4" fill="none" stroke="#fff" stroke-width="0.6"/></svg>Crestafinancialgroup.example.</li>
        </ul>
      </div>
      <div class="tagline">Para un futuro mas seguro!</div>
    </article>
  </section>
  <div class="option-label option-label--b">B</div>
</div>
</body>
</html>
```